We need a business card design for a new brand within our existing financial marketing business. Our new brand is www.quellpath.co.uk

We attach various logo files - please use the version that will produce the sharpest image on the business card.

We are flexible about shape of card etc. Please think outside the box as to what goes on front and what goes on back of the card.

The card needs to be corporate, but really catch the eye ( e.g. premium translucent cards on plastic etc or metal cards or shiny surface etc )

We want to be able to amend the card (once the design has been agreed ) to add additional staff details, but the text to go on it will be generic

Details to go on card ( for the first generic one) are fairly minimal as we don't like cluttered business cards:-

Owen Tabler
Managing Director

Mobile: 07841 552 078
Email: o.tabler@quellpath.co.uk

```html
<!DOCTYPE html>
<html lang="en">
<head>
<meta charset="utf-8">
<title>Quellpath Business Card</title>
<link rel="stylesheet" href="https://fonts.googleapis.com/css2?family=Lato:wght@400;700&family=Montserrat:wght@300&display=swap">
<style>
  :root {
    --backdrop: #e6e6e6;
    --card: #111213;
    --card-edge: #0b0b0c;
    --gold: #d2a22c;
    --blue: #1f86c4;
    --white: #f2f2f2;
    --muted: #dcdcdc;
  }
  * { margin: 0; padding: 0; box-sizing: border-box; }
  html, body {
    width: 1200px; height: 720px; overflow: hidden;
    background: var(--backdrop);
  }
  .canvas { position: relative; width: 1200px; height: 720px; }
  .card {
    position: absolute; top: 241px;
    width: 420px; height: 240px;
    background: linear-gradient(135deg, #1a1b1c 0%, var(--card) 45%, var(--card-edge) 100%);
  }
  .card--front { left: 147px; }
  .card--back { left: 633px; }

  .marker {
    position: absolute; left: 0; top: 101px;
    width: 0; height: 0;
    border-top: 19px solid transparent;
    border-bottom: 19px solid transparent;
    border-left: 19px solid var(--gold);
  }
  .person { position: absolute; left: 30px; top: 105px; font-family: 'Lato', sans-serif; }
  .person__name { color: var(--gold); font-weight: 700; font-size: 13.5px; line-height: 1.1; }
  .person__role { color: var(--white); font-size: 10px; line-height: 1.3; }

  .wordmark {
    font-family: 'Montserrat', sans-serif; font-weight: 300;
    color: var(--blue); letter-spacing: 0.5px; white-space: nowrap;
  }
  .card--front .wordmark { position: absolute; right: 24px; top: 103px; font-size: 30px; }
  .card--back .wordmark {
    position: absolute; left: 0; right: 0; top: 92px;
    text-align: center; font-size: 48px; line-height: 1.1;
  }

  .contacts {
    position: absolute; right: 24px; top: 168px;
    list-style: none; font-family: 'Lato', sans-serif;
    font-size: 10px; color: var(--muted);
  }
  .contacts__item {
    display: flex; justify-content: flex-end; align-items: center;
    gap: 10px; height: 12px;
  }
  .contacts__icon { width: 10px; height: 10px; flex: none; }
</style>
</head>
<body>
<main class="canvas">
  <section class="card card--front" aria-label="Card front">
    <span class="marker"></span>
    <div class="person">
      <p class="person__name">Owen Tabler</p>
      <p class="person__role">Managing Director</p>
    </div>
    <p class="wordmark">quellpath</p>
    <ul class="contacts">
      <li class="contacts__item">07841 552 078
        <svg class="contacts__icon" viewBox="0 0 10 10" aria-hidden="true"><rect x="2.5" y="0.8" width="5" height="8.4" rx="0.8" fill="none" stroke="#d2a22c" stroke-width="1.1"/><rect x="4.2" y="7.4" width="1.6" height="0.8" fill="#d2a22c"/></svg>
      </li>
      <li class="contacts__item">o.tabler@quellpath.co.uk
        <svg class="contacts__icon" viewBox="0 0 10 10" aria-hidden="true"><rect x="0.5" y="2" width="9" height="6.5" fill="#d2a22c"/><path d="M0.8 2.3 L5 5.6 L9.2 2.3" fill="none" stroke="#111213" stroke-width="0.8"/></svg>
      </li>
      <li class="contacts__item">www.quellpath.co.uk
        <svg class="contacts__icon" viewBox="0 0 10 10" aria-hidden="true"><rect x="0.8" y="1.5" width="8.4" height="5.6" fill="none" stroke="#d2a22c" stroke-width="1.1"/><rect x="3" y="8" width="4" height="1" fill="#d2a22c"/></svg>
      </li>
    </ul>
  </section>

  <section class="card card--back" aria-label="Card back">
    <p class="wordmark">quellpath</p>
  </section>
</main>
</body>
</html>
```